Business Card Design Project

I have a two letter domain name qo.com.au (lower case font please). I want a business card, cum logo that is die cut (around the qo segment at least) that fits standard business card size.
qo is all about what 'I am' - a journalist, blogger, analyst, commentator. My mantra is "I wander so qo'.
The reverse of the card only needs my name Lon Fitch, email lon@qo.com.au and mobile +61 400 555 817
Target Market(s)
Mainly people that will use my professional writing services and suppliers that will provide product for review
Industry/Entity Type
Business
Requirements
Must have
- One side is qo.com.au (hint - the .com.au can be vertical or horizontal to fit - the qo should be as large as possible).
The other requires large size font name, email and phone details (so no one needs glasses to read it).
The die cut can be just to highlight the qo segment - need not be around the whole card.
Font used in the past was Belwe (old style - very much like the i used in the information symbol).
Colours - no preference - prefer two colour to process colour but can also be an outline font instead of solid colour.

```html
<!DOCTYPE html>
<html lang="en">
<head>
<meta charset="utf-8">
<title>qo.com.au business card</title>
<link rel="stylesheet" href="https://fonts.googleapis.com/css2?family=Jost:wght@400;600&display=swap">
<style>
  :root {
    --backdrop: #e4e4e2;
    --charcoal: #4a4a4a;
    --cyan: #00f2ff;
    --white: #ffffff;
    --mark-tone: #9a9a98;
  }
  * { margin: 0; padding: 0; box-sizing: border-box; }
  html, body {
    width: 1200px;
    height: 1000px;
    overflow: hidden;
    background: var(--backdrop);
    font-family: "Jost", "Futura", sans-serif;
  }
  .canvas {
    position: relative;
    width: 1200px;
    height: 1000px;
  }
  .card {
    position: absolute;
    width: 300px;
    height: 540px;
    display: flex;
    flex-direction: column;
    align-items: center;
  }
  .card--front {
    left: 230px;
    top: 190px;
    background: var(--charcoal);
  }
  .card--back {
    left: 640px;
    top: 330px;
    background: var(--cyan);
  }
  .brand-mark {
    margin-top: 130px;
    height: 160px;
    display: flex;
    align-items: center;
    justify-content: center;
    font-weight: 600;
    font-size: 150px;
    line-height: 1;
    color: var(--mark-tone);
    letter-spacing: -2px;
  }
  .domain {
    margin-top: 28px;
    font-weight: 400;
    font-size: 36px;
    line-height: 1;
    color: var(--white);
  }
  .tagline {
    margin-top: 6px;
    font-weight: 400;
    font-size: 16px;
    color: var(--cyan);
  }
  .contact-name {
    margin-top: 46px;
    font-weight: 600;
    font-size: 20px;
    color: var(--charcoal);
  }
  .contact-email {
    margin-top: 24px;
    font-weight: 400;
    font-size: 17px;
    color: var(--charcoal);
  }
  .contact-phone {
    margin-top: 18px;
    font-weight: 400;
    font-size: 20px;
    color: var(--charcoal);
  }
</style>
</head>
<body>
  <main class="canvas">
    <section class="card card--front" aria-label="Card front">
      <div class="brand-mark">qo</div>
      <p class="domain">qo.com.au</p>
      <p class="tagline">I wander so qo</p>
    </section>
    <section class="card card--back" aria-label="Card back">
      <div class="brand-mark">qo</div>
      <p class="contact-name">Lon Fitch</p>
      <p class="contact-email">lon@qo.com.au</p>
      <p class="contact-phone">+61 400 555 817</p>
    </section>
  </main>
</body>
</html>
```